We need a new design for our construction website

We need a new website for our wordpress site kerrowmade.co.nz

It needs to be only a few pages but sleek in design and responsive, beautifully showcasing our images and video. Currently we have
1. home
2. about us
3. contact
We need either a front page that is designed much better to showcase more content, or potentially a projects page which has images from our builds. We don't have a lot of content so the content we do have needs to be maximised by image, rather than project.

Target Market(s)

High end residential construction and renovation projects, people wanting to build a nice home, clients based in Mount Maunganui, Tauranga.

Coding

Font styles to use
Sans Serif

Colors

Designer to choose only greyscale colors for use in the design.

Requirements
Must have
• A sleek design, architectural

```html
<!DOCTYPE html>
<html lang="en">
<head>
<meta charset="utf-8">
<title>Kerrowmade — Construction</title>
<link href="https://fonts.googleapis.com/css2?family=Poppins:wght@300;400;500;600;700;800&display=swap" rel="stylesheet">
<style>
:root{
  --band:#b9b9b9;
  --band-soft:#cfcfcf;
  --accent:#8e8e8e;
  --accent-light:#a8a8a8;
  --ink:#111111;
  --dark:#1d1d1f;
  --night:#0b0b0c;
  --grey:#8b8b8b;
  --line:#bdbdbd;
  --text:#444444;
  --white:#ffffff;
}
*{box-sizing:border-box;margin:0;padding:0}
html,body{width:1200px;height:3714px;overflow:hidden}
body{position:relative;font-family:'Poppins',sans-serif;color:var(--text);background:var(--white)}
.abs{position:absolute}
a{color:inherit;text-decoration:none}

/* header */
.site-header{position:absolute;left:0;top:0;width:1200px;height:104px;background:rgba(20,20,22,.92);z-index:3}
.brand{position:absolute;left:144px;top:22px;display:flex;align-items:center;gap:16px}
.brand-square{width:56px;height:56px;border:2px solid #9e9e9e}
.brand-name{font-weight:300;font-size:31px;letter-spacing:14px;color:#9e9e9e}
.nav-item{position:absolute;top:42px;font-size:12px;color:var(--white);font-weight:400}
.nav-home{left:574px;top:0;width:108px;height:87px;background:#3d3d40;text-align:center;padding-top:42px}
.nav-home::after{content:"";position:absolute;left:53px;top:66px;width:1px;height:20px;background:var(--white)}
.search{position:absolute;left:927px;top:35px;width:116px;height:33px;border:1px solid #8a8a8a;border-radius:17px;color:var(--white);font-size:12px;text-align:center;line-height:31px}

/* hero */
.hero{position:absolute;left:0;top:0;width:1200px;height:747px;background:linear-gradient(180deg,#434345 0%,#7c7c7e 45%,#505052 100%)}
.hero-copy{position:absolute;left:424px;top:296px;width:400px;text-align:center;color:var(--white)}
.hero-title{font-size:52px;font-weight:700;line-height:1}
.hero-text{margin-top:20px;font-size:21px;line-height:32px;font-weight:400}
.btn-dark{position:absolute;left:548px;top:519px;width:156px;height:48px;background:var(--ink);color:var(--white);font-size:15px;display:flex;align-items:center;justify-content:center;gap:20px}
.hero-arrow{position:absolute;top:373px}

/* info strip */
.info-strip{position:absolute;left:144px;top:724px;width:900px;height:55px;background:var(--band-soft);font-size:12px;color:#222}
.info-strip .sep{position:absolute;top:16px;width:1px;height:22px;background:#8a8a8a}
.social{display:inline-block;width:23px;height:23px;border:1.5px solid #222;border-radius:50%}

/* about */
.about{position:absolute;left:144px;top:873px;width:900px;height:471px}
.about-panel{position:absolute;left:0;top:0;width:463px;height:471px;background:var(--dark)}
.about-photo{position:absolute;left:463px;top:0;width:437px;height:471px;background:linear-gradient(160deg,#e4e4e4 0%,#b4b4b4 45%,#3f3f41 100%)}
.section-title{font-weight:800;letter-spacing:.5px;line-height:1}
.about-title{position:absolute;left:32px;top:54px;font-size:49px;color:var(--accent-light)}
.about-rule{position:absolute;left:32px;top:111px;width:81px;height:2px;background:var(--accent-light)}
.about-text{position:absolute;left:34px;top:144px;width:395px;font-size:12.6px;line-height:18px;color:#e2e2e2;text-align:justify}
.btn-light{position:absolute;left:38px;top:377px;width:155px;height:48px;background:var(--white);color:#333;font-size:14px;display:flex;align-items:center;justify-content:center;gap:14px}

/* services */
.service{position:absolute;top:1421px;width:226px;height:370px;text-align:center}
.service.active{background:var(--white);box-shadow:0 2px 10px rgba(0,0,0,.14)}
.service svg{position:absolute;left:48px;top:22px}
.service h3{position:absolute;left:0;top:197px;width:100%;font-size:15px;font-weight:600;color:var(--ink)}
.service.active h3{color:var(--accent)}
.service p{position:absolute;left:13px;top:228px;width:200px;font-size:9.3px;line-height:13.8px;color:#555}

/* projects */
.projects-band{position:absolute;left:143px;top:1866px;width:901px;height:561px;background:var(--band)}
.projects-title{position:absolute;left:0;top:1910px;width:1200px;text-align:center;font-size:52px;color:var(--white)}
.project{position:absolute;top:1996px;width:300px;height:355px}
.project-label{position:absolute;left:0;top:157px;width:50px;height:198px;background:#151515;color:var(--white)}
.project-label span{position:absolute;left:25px;bottom:14px;transform-origin:left bottom;transform:rotate(-90deg) translateY(7px);font-size:11px;font-weight:600;white-space:nowrap;width:0}
.project-label::before{content:"";position:absolute;left:24px;top:14px;width:1px;height:70px;background:#777}
.project-label.light{background:var(--white);color:var(--ink)}
.dot{position:absolute;top:2385px;width:11px;height:11px;border:1px solid #6a6a6a;border-radius:50%}
.dot.on{border:2px solid var(--white);width:15px;height:15px;top:2383px}

/* testimonial */
.testimonials{position:absolute;left:0;top:2429px;width:1200px;height:463px;background:repeating-linear-gradient(90deg,#0d0d0e 0 6px,#121214 6px 12px)}
.quote-box{position:absolute;left:143px;top:2567px;width:901px;height:222px;border:1px solid #2e2e30}
.quote-name{position:absolute;left:241px;top:2640px;font-size:20px;color:var(--accent-light);font-weight:500}
.quote-text{position:absolute;left:240px;top:2676px;width:760px;text-align:center;font-size:12px;line-height:18.5px;color:#d8d8d8}
.thumb{position:absolute;top:2757px;width:60px;height:60px;border-radius:50%;border:2px solid var(--white)}

/* contact */
.contact{position:absolute;left:0;top:2892px;width:1200px;height:520px;background:linear-gradient(135deg,#ffffff 0%,#f0f0f0 45%,#e2e2e2 100%)}
.contact-person{position:absolute;left:144px;top:2978px;width:238px;height:434px;background:linear-gradient(180deg,#e8a640 0%,#b5805e 18%,#3f6b4f 45%,#2f4a3a 80%,#2c3038 100%);border-radius:110px 110px 0 0}
.contact-title{position:absolute;left:406px;top:2964px;font-size:56px;color:var(--ink)}
.contact-sub{position:absolute;left:407px;top:3024px;font-size:23px;line-height:30px;font-weight:300;color:#333}
.field{position:absolute;border-bottom:1px solid #9a9a9a;font-size:11px;color:#555;height:22px}
.btn-send{position:absolute;left:408px;top:3314px;width:635px;height:35px;background:var(--ink);color:var(--white);font-size:12px;font-weight:700;display:flex;align-items:center;justify-content:center;gap:12px}

/* footer */
.footer-brand{position:absolute;left:144px;top:3486px;display:flex;align-items:center;gap:14px}
.footer-brand .brand-square{width:40px;height:40px;border:2px solid #8a8a8a}
.footer-brand .brand-name{font-size:21px;letter-spacing:10px;color:#777}
.footer-text{position:absolute;left:144px;top:3545px;width:270px;font-size:12px;line-height:16.5px;color:#444;text-align:justify}
.footer-follow{position:absolute;left:144px;top:3613px;font-size:11.5px;font-weight:600;color:var(--ink);display:flex;align-items:center;gap:12px}
.footer-follow .social{width:18px;height:18px;border:1px solid #333}
.footer-follow .social.fill{background:var(--accent-light);border-color:var(--accent-light)}
.footer-head{position:absolute;top:3480px;font-size:22px;font-weight:600;color:#222}
.footer-head::before{content:"";position:absolute;left:-48px;top:16px;width:35px;height:1px;background:var(--accent-light)}
.footer-list{position:absolute;left:544px;top:3543px;list-style:none;font-size:12px;color:#222}
.footer-list li{height:26px;position:relative;padding-left:17px}
.footer-list li::before{content:"";position:absolute;left:0;top:6px;width:6px;height:6px;border-radius:50%;background:#111}
.footer-list li.current{color:var(--accent-light)}
.footer-list li.current::before{background:var(--accent-light)}
.footer-contact{position:absolute;left:885px;font-size:12px;color:#333;line-height:17px;display:flex;gap:14px}
.copyright{position:absolute;left:0;top:3685px;width:1200px;height:29px;background:#252527;color:#ddd;font-size:10px;text-align:center;line-height:29px}
</style>
</head>
<body>

<!-- hero -->
<section class="hero" role="img" aria-label="Upward view of glass skyscrapers in a city centre, in grey tones"></section>
<svg class="abs" style="left:0;top:0" width="1200" height="747" aria-hidden="true">
  <polygon points="624,166 842,263 842,458 624,555 406,458 406,263" fill="rgba(190,190,190,.3)" stroke="rgba(230,230,230,.6)" stroke-width="2"/>
  <polyline points="406,263 624,360 842,263" fill="none" stroke="rgba(230,230,230,.25)" stroke-width="1"/>
  <line x1="624" y1="360" x2="624" y2="555" stroke="rgba(230,230,230,.25)"/>
</svg>
<header class="site-header">
  <div class="brand"><span class="brand-square"></span><span class="brand-name">KERROWMADE</span></div>
  <a class="nav-item nav-home">HOME</a>
  <a class="nav-item" style="left:729px">ABOUT</a>
  <a class="nav-item" style="left:838px">CONTACT</a>
  <div class="search">Search Here</div>
</header>
<div class="hero-copy">
  <h1 class="hero-title">OUR VISION</h1>
  <p class="hero-text">is to build beautiful, efficient homes with the best building technologies available that our customers are proud to own.</p>
</div>
<a class="btn-dark">More Info
  <svg width="26" height="10"><line x1="0" y1="5" x2="24" y2="5" stroke="#fff" stroke-width="1.5"/><polyline points="19,1 24,5 19,9" fill="none" stroke="#fff" stroke-width="1.5"/></svg>
</a>
<svg class="hero-arrow" style="left:16px" width="62" height="62"><circle cx="31" cy="31" r="28" fill="none" stroke="#fff" stroke-width="3"/><line x1="14" y1="31" x2="46" y2="31" stroke="#fff" stroke-width="3"/><polyline points="26,19 14,31 26,43" fill="none" stroke="#fff" stroke-width="3"/></svg>
<svg class="hero-arrow" style="left:1122px" width="62" height="62"><circle cx="31" cy="31" r="28" fill="none" stroke="#fff" stroke-width="3"/><line x1="16" y1="31" x2="48" y2="31" stroke="#fff" stroke-width="3"/><polyline points="36,19 48,31 36,43" fill="none" stroke="#fff" stroke-width="3"/></svg>

<!-- info strip -->
<div class="info-strip">
  <svg class="abs" style="left:94px;top:15px" width="24" height="24"><path d="M5 3 L10 3 L12 8 L9 10 Q12 15 15 16 L17 13 L22 15 L22 20 Q12 22 4 12 Q2 7 5 3Z" fill="none" stroke="#222" stroke-width="1.6"/></svg>
  <span class="abs" style="left:138px;top:20px">027 481 3092</span>
  <span class="sep" style="left:263px"></span>
  <span class="abs" style="left:314px;top:17px;font-size:14px;font-weight:600">Follow Us On:</span>
  <span class="abs" style="left:423px;top:16px"><span class="social"></span></span>
  <span class="abs" style="left:463px;top:16px"><span class="social"></span></span>
  <span class="abs" style="left:503px;top:16px"><span class="social"></span></span>
  <span class="sep" style="left:574px"></span>
  <svg class="abs" style="left:620px;top:18px" width="26" height="19"><rect x="1" y="1" width="24" height="17" fill="#222"/><polyline points="1,1 13,10 25,1" fill="none" stroke="#cfcfcf" stroke-width="1.5"/></svg>
  <span class="abs" style="left:658px;top:20px">mara@kerrowmade.co.nz</span>
</div>

<!-- about -->
<section class="about">
  <div class="about-panel">
    <h2 class="section-title about-title">ABOUT US</h2>
    <span class="about-rule"></span>
    <p class="about-text">Lorem ipsum dolor sit amet, consectetur adipiscing elit, sed do eiusmod tempor incididunt ut labore et dolore magna aliqua. Ut enim ad minim veniam, quis nostrud exercitation ullamco laboris nisi ut aliquip ex ea commodo consequat. Duis aute irure dolor in reprehenderit in voluptate velit esse cillum dolore eu fugiat nulla pariatur. Excepteur sint occaecat cupidatat non proident, sunt in culpa qui officia deserunt mollit anim id est laborum.Lorem ipsum dolor sit amet, consectetur adipiscing elit, sed do eiusmod tempor incididunt ut labore et dolore magna aliqua. Ut enim ad minim veniam, quis nostrud exercitation ullamco laboris nisi ut aliquip ex ea commodo consequat.</p>
    <a class="btn-light">Read More
      <svg width="26" height="10"><line x1="0" y1="5" x2="24" y2="5" stroke="#333" stroke-width="1.5"/><polyline points="19,1 24,5 19,9" fill="none" stroke="#333" stroke-width="1.5"/></svg>
    </a>
  </div>
  <div class="about-photo" role="img" aria-label="Engineers in hard hats looking up at high-rise towers under construction"></div>
  <svg class="abs" style="left:463px;top:207px" width="16" height="32"><polygon points="0,0 14,16 0,32" fill="#1d1d1f"/></svg>
</section>

<!-- services -->
<article class="service" style="left:138px">
  <svg width="130" height="150" viewBox="0 0 130 150"><polygon points="65,6 121,38 121,112 65,144 9,112 9,38" fill="none" stroke="#a6a6a6" stroke-width="9"/><polygon points="65,20 109,45 109,105 65,130 21,105 21,45" fill="#fff" stroke="#e2e2e2" stroke-width="2"/>
    <polygon points="40,76 65,54 90,76" fill="none" stroke="#8e8e8e" stroke-width="3"/><polyline points="47,70 47,98 83,98 83,70" fill="none" stroke="#8e8e8e" stroke-width="3"/><rect x="59" y="82" width="12" height="16" fill="none" stroke="#8e8e8e" stroke-width="3"/></svg>
  <h3>Design and Build</h3>
  <p>The Design and Build process streamlines your home construction project ensuring your architect or designer and builder are on the same page from day one meaning you get the dream home you've always wanted.</p>
</article>
<article class="service active" style="left:361px">
  <svg width="130" height="150" viewBox="0 0 130 150"><polygon points="65,6 121,38 121,112 65,144 9,112 9,38" fill="none" stroke="#8e8e8e" stroke-width="9"/><polygon points="65,20 109,45 109,105 65,130 21,105 21,45" fill="#fff" stroke="#e2e2e2" stroke-width="2"/>
    <line x1="46" y1="56" x2="84" y2="94" stroke="#444" stroke-width="5" stroke-linecap="round"/><line x1="84" y1="56" x2="46" y2="94" stroke="#444" stroke-width="5" stroke-linecap="round"/><circle cx="84" cy="56" r="7" fill="none" stroke="#444" stroke-width="3"/></svg>
  <h3>Renovations &amp; Additions</h3>
  <p>Improving the layout and functionality of your home doesn't mean having to build from scratch, renovations and additions can modernise your home, improve things like energy efficiency and the way that your building "performs."</p>
</article>
<article class="service" style="left:582px">
  <svg width="130" height="150" viewBox="0 0 130 150"><polygon points="65,6 121,38 121,112 65,144 9,112 9,38" fill="none" stroke="#a6a6a6" stroke-width="9"/><polygon points="65,20 109,45 109,105 65,130 21,105 21,45" fill="#fff" stroke="#e2e2e2" stroke-width="2"/>
    <polyline points="64,56 46,56 46,96 86,96 86,78" fill="none" stroke="#8e8e8e" stroke-width="3"/><line x1="62" y1="80" x2="86" y2="56" stroke="#8e8e8e" stroke-width="4"/></svg>
  <h3>Project Management</h3>
  <p>We specialise in managing your entire build project. From liaising with your designer, engineers, advising you on the best building materials, sourcing trustworthy subcontractors and scheduling and managing the roll-out of each build stage. We are experienced and have a reputation for on-time, on-budget builds.</p>
</article>
<article class="service" style="left:806px">
  <svg width="130" height="150" viewBox="0 0 130 150"><polygon points="65,6 121,38 121,112 65,144 9,112 9,38" fill="none" stroke="#a6a6a6" stroke-width="9"/><polygon points="65,20 109,45 109,105 65,130 21,105 21,45" fill="#fff" stroke="#e2e2e2" stroke-width="2"/>
    <path d="M56 86 Q48 78 50 68 Q54 56 65 56 Q76 56 80 68 Q82 78 74 86 Z" fill="none" stroke="#8e8e8e" stroke-width="3"/><line x1="58" y1="92" x2="72" y2="92" stroke="#8e8e8e" stroke-width="3"/><line x1="60" y1="98" x2="70" y2="98" stroke="#8e8e8e" stroke-width="3"/></svg>
  <h3>Build Smarter</h3>
  <p>We are passionate about building smarter, even better than the building code. When it comes to energy efficiency, a warm and healthy home performs with true efficiency. What do we mean? Comfort, thermally-broken, well designed and the best quality materials to match your project budget.</p>
</article>

<!-- projects -->
<div class="projects-band"></div>
<h2 class="section-title projects-title">OUR PROJECTS</h2>
<figure class="project" style="left:0;background:linear-gradient(135deg,#eef0f2 0%,#b8a894 50%,#6d7f8e 100%)" role="img" aria-label="Open living room with timber deck looking onto a lake">
  <div class="project-label"><span>PROJECT 01</span></div></figure>
<figure class="project" style="left:300px;background:linear-gradient(160deg,#9fb7c9 0%,#2a6a9a 45%,#1f4e73 80%,#4d7a3e 100%)" role="img" aria-label="Modern glass office building with blue facade">
  <div class="project-label light"><span>PROJECT 02</span></div>
  <svg class="abs" style="left:133px;top:163px" width="36" height="36"><circle cx="14" cy="14" r="11" fill="none" stroke="#fff" stroke-width="3"/><line x1="22" y1="22" x2="33" y2="33" stroke="#fff" stroke-width="4"/></svg></figure>
<figure class="project" style="left:600px;background:linear-gradient(180deg,#e8ecef 0%,#d9c7a8 40%,#5ba8dc 70%,#c9d2d8 100%)" role="img" aria-label="White villa with balconies behind a swimming pool">
  <div class="project-label"><span>PROJECT 03</span></div></figure>
<figure class="project" style="left:900px;background:linear-gradient(180deg,#c9d7e6 0%,#a9a39a 40%,#5d5e62 75%,#7ab24f 100%)" role="img" aria-label="Grey two-storey suburban house with front lawn">
  <div class="project-label"><span>PROJECT 04</span></div></figure>
<span class="dot" style="left:543px"></span>
<span class="dot" style="left:565px"></span>
<span class="dot on" style="left:584px"></span>
<span class="dot" style="left:609px"></span>
<span class="dot" style="left:632px"></span>

<!-- testimonial -->
<section class="testimonials"></section>
<div class="quote-box"></div>
<div class="abs" style="left:531px;top:2507px;width:130px;height:130px;border-radius:50%;border:4px solid #2b2b2b;background:linear-gradient(180deg,#d8d2c6 0%,#a0651f 55%,#5a4a3a 100%)" role="img" aria-label="Living room with a leather sofa and lamp"></div>
<svg class="abs" style="left:171px;top:2648px" width="42" height="34"><path d="M16 4 Q4 6 4 18 L4 30 L16 30 L16 18 L9 18 Q10 10 17 9Z M38 4 Q26 6 26 18 L26 30 L38 30 L38 18 L31 18 Q32 10 39 9Z" fill="none" stroke="#ddd" stroke-width="2"/></svg>
<p class="quote-name">Hana</p>
<p class="quote-text">Our home is the envy of many friends. It holds the warmth incredibly through the winter and is perfectly cool in the summer. The ease of design has made it not only very smart with a modern feel but also with its strong robust construction it feels safe and secure for our young family. We love our home!</p>
<span class="thumb" style="left:424px;background:linear-gradient(180deg,#c8bfb0,#a0521e)" role="img" aria-label="Lounge interior"></span>
<span class="thumb" style="left:515px;background:linear-gradient(180deg,#e6e2dc,#9c8e80)" role="img" aria-label="Dining room interior"></span>
<span class="thumb" style="left:609px;background:linear-gradient(180deg,#f4f4f4,#c9cfd6)" role="img" aria-label="Bright white bedroom"></span>
<span class="thumb" style="left:703px;background:linear-gradient(180deg,#dfe8ee,#b69c78)" role="img" aria-label="Kitchen interior"></span>
<svg class="abs" style="left:897px;top:2754px" width="44" height="16"><line x1="2" y1="8" x2="42" y2="8" stroke="#555" stroke-width="2"/><polyline points="10,1 2,8 10,15" fill="none" stroke="#555" stroke-width="2"/></svg>
<svg class="abs" style="left:953px;top:2754px" width="44" height="16"><line x1="2" y1="8" x2="42" y2="8" stroke="#bdbdbd" stroke-width="2"/><polyline points="34,1 42,8 34,15" fill="none" stroke="#bdbdbd" stroke-width="2"/></svg>

<!-- contact -->
<section class="contact"></section>
<div class="contact-person" role="img" aria-label="Smiling builder in an orange hard hat and green shirt with arms crossed"></div>
<h2 class="section-title contact-title">CONTACT US</h2>
<p class="contact-sub">For a free no obligation chat about your building project -</p>
<div class="field" style="left:408px;top:3084px;width:311px">Name</div>
<div class="field" style="left:734px;top:3084px;width:309px">Subject</div>
<div class="field" style="left:408px;top:3123px;width:635px">Phone Number</div>
<div class="field" style="left:408px;top:3166px;width:635px">E-Mail</div>
<div class="field" style="left:408px;top:3209px;width:635px;height:66px">Message</div>
<a class="btn-send">GET IN TOUCH
  <svg width="14" height="14"><polygon points="1,7 13,1 8,13 7,8" fill="#fff"/></svg>
</a>

<!-- footer -->
<div class="footer-brand"><span class="brand-square"></span><span class="brand-name">KERROWMADE</span></div>
<p class="footer-text">Lorem ipsum dolor sit amet, consectetur adipiscing elit, sed do eiusmod tempor incididunt ut labore et dolore...</p>
<div class="footer-follow">Follow Us On: <span class="social fill"></span><span class="social"></span><span class="social"></span></div>

<h4 class="footer-head" style="left:544px">Quick Links</h4>
<ul class="footer-list">
  <li class="current">HOME</li>
  <li>ABOUT</li>
  <li>CONTACT</li>
</ul>

<h4 class="footer-head" style="left:881px">CONTACT US</h4>
<div class="footer-contact" style="top:3541px">
  <svg width="10" height="14"><path d="M5 13 Q0 6 0 5 A5 5 0 0 1 10 5 Q10 6 5 13Z" fill="#a8a8a8"/><circle cx="5" cy="5" r="2" fill="#fff"/></svg>
  <span>Lorem ipsum Public 1234,<br>Somestreet NY 0123</span></div>
<div class="footer-contact" style="top:3586px">
  <svg width="12" height="12"><polygon points="0,6 12,0 8,12 6,7" fill="#a8a8a8"/></svg>
  <span>mara@kerrowmade.co.nz</span></div>
<div class="footer-contact" style="top:3621px">
  <svg width="12" height="12"><path d="M2 1 L5 1 L6 4 L4 5 Q6 8 8 9 L9 7 L12 8 L12 11 Q6 12 1 6 Q0 3 2 1Z" fill="#a8a8a8"/></svg>
  <span>027 481 3092</span></div>

<div class="copyright">©2020 KERROWMADE. All Rights Reserved.</div>

</body>
</html>
```